Ridgecrest Balusters Website Redesign

I want a fresh new design for my website. Original website
www.ridgecrestbalusters.example. Will need to add additional photos for winning designer. Please use the basic layout for new design. Looking to get a more modern, functional site to attract new customer and ne bale to highlight past projects. Need it to be easy to navigate and get in touch with me for inquiries.

Target Market(s)

Builders and home owners in WA state

Industry/Entity Type

Building, Construction, Deck building

Coding

Coded - Design and coding required

Number of Pages Required

5+ page

Font styles to use
Sans Serif

Colors
0054AA
0677BA
7BADD7
CADEEF
E8F1F8
0094D4
00A9DD
6FCCEA
C7EBF8
E9F6FB
00AB8E
00BBA5
67D7C9
C6EFE9
E9F9F6
59FF00
82FF00
B8FF75
E3FFCB
F4FFEA

Requirements
Must have
• Will need to add more photos of completed projects
Nice to have
• Fresh take on old website, something modern
Should not have
• Nothing comes to mind

```html
<!DOCTYPE html>
<html lang="en">
<head>
<meta charset="utf-8">
<title>Ridgecrest Balusters</title>
<link rel="stylesheet" href="https://fonts.googleapis.com/css2?family=DM+Sans:wght@400;500;600;700&display=swap">
<style>
  :root {
    --navy: #0054AA;
    --ocean: #0677BA;
    --sky: #0094D4;
    --teal: #00AB8E;
    --teal-bright: #00BBA5;
    --lime: #82FF00;
    --mist: #E8F1F8;
    --ink: #1f2f3f;
    --muted: #4f5d6b;
    --paper: #ffffff;
  }
  * { box-sizing: border-box; margin: 0; padding: 0; }
  html, body { width: 1200px; height: 1010px; overflow: hidden; background: var(--paper); }
  body { font-family: "DM Sans", Arial, sans-serif; color: var(--ink); position: relative; }

  .hero { position: absolute; left: 0; top: 0; width: 1200px; height: 487px; }
  .brand { position: absolute; left: 61px; top: 19px; font-size: 14px; font-weight: 500; line-height: 14.5px; letter-spacing: 0.2px; color: var(--navy); }
  .nav { position: absolute; left: 190px; top: 25px; display: flex; gap: 24px; font-size: 11.6px; color: var(--muted); }
  .hero-photo {
    position: absolute; left: 640px; top: 0; width: 560px; height: 487px;
    background:
      linear-gradient(160deg, rgba(88,92,92,0) 45%, rgba(70,72,72,0.85) 70%),
      linear-gradient(200deg, #9fc78a 0%, #5f8f4a 30%, #8a9ca6 55%, #6b6f70 80%, #4f5253 100%);
  }
  .contact-btn {
    position: absolute; left: 1056px; top: 18px; width: 111px; height: 29px;
    background: var(--teal); color: #fff; border-radius: 2px;
    font-size: 11.6px; font-weight: 500; display: flex; align-items: center; justify-content: center;
  }
  .hero-title {
    position: absolute; left: 57px; top: 158px; width: 420px;
    font-size: 52px; line-height: 56px; font-weight: 600; letter-spacing: -1.6px; color: var(--navy);
  }
  .hero-lede {
    position: absolute; left: 61px; top: 352px; width: 350px;
    font-size: 11.4px; line-height: 19.8px; color: var(--muted);
  }

  .about {
    position: absolute; left: 0; top: 487px; width: 1200px; height: 523px;
    background: linear-gradient(120deg, var(--navy) 0%, var(--ocean) 100%); color: #fff;
  }
  .about-heading { position: absolute; left: 170px; top: 78px; width: 270px; font-size: 22px; line-height: 29px; font-weight: 500; letter-spacing: 0.2px; }
  .about-meta { position: absolute; left: 170px; font-size: 11.4px; color: var(--mist); }
  .about-meta.license { top: 158px; }
  .about-meta.formed { top: 187px; }
  .about-copy { position: absolute; left: 170px; width: 440px; font-size: 11.4px; line-height: 19.4px; }
  .about-copy.first { top: 231px; }
  .about-copy.second { top: 347px; }
  .about-copy strong { font-weight: 600; color: var(--lime); }

  .brand-panel {
    position: absolute; left: 764px; top: 101px; width: 333px; height: 316px;
    background: var(--paper); display: flex; flex-direction: column; align-items: center; justify-content: center; gap: 18px;
  }
  .brand-panel .mark { width: 40px; height: 40px; background: var(--teal); }
  .brand-panel .name { font-size: 34px; line-height: 40px; font-weight: 600; color: var(--navy); text-align: center; }
</style>
</head>
<body>
  <header class="hero">
    <div class="brand">RIDGECREST<br>BALUSTERS</div>
    <nav class="nav">
      <span>Home</span><span>Products</span><span>About</span><span>Railing Project</span><span>Remodel Project</span>
    </nav>
    <div class="hero-photo" role="img" aria-label="Photo of a house balcony with glass panel railing surrounded by trees"></div>
    <div class="contact-btn">Contact</div>
    <h1 class="hero-title">Building Dreams, One Home at a Time.</h1>
    <p class="hero-lede">Your trusted partner for quality construction, innovative designs, and seamless homeownership experiences. Let's create the perfect space together.</p>
  </header>

  <section class="about">
    <h2 class="about-heading">LICENSED, INSURED, &amp; BONDED</h2>
    <p class="about-meta license">WA GC LICENSE # RIDGEBB417KT</p>
    <p class="about-meta formed">Formed in 2020</p>
    <p class="about-copy first"><strong>At Ridgecrest Balusters,</strong> we believe that every outdoor space deserves the perfect blend of style, safety, and durability. Serving homeowners, builders, and commercial developers across the Washington State, we specialize in crafting custom railing systems designed to withstand the region's unique climate while enhancing the beauty of your outdoor living spaces.</p>
    <p class="about-copy second">With a focus on premium materials, expert craftsmanship, and exceptional customer service, <strong>Ridgecrest Balusters</strong> is proud to be the trusted partner for both residential and commercial railing projects. Whether you’re looking to complement a new deck, add a modern touch to your balcony, or create a secure and stunning barrier for a commercial space, we’ve got the perfect solution for you.</p>
    <div class="brand-panel">
      <div class="mark"></div>
      <div class="name">RIDGECREST<br>BALUSTERS</div>
    </div>
  </section>
</body>
</html>
```